New letter head for Air Conditioning business

We need a new professional letter head design to suit our new re-branded air conditioning business. Our new logo is attached

```html
<!DOCTYPE html>
<html lang="en">
<head>
<meta charset="utf-8">
<title>Nordvale Letterhead</title>
<link rel="stylesheet" href="https://fonts.googleapis.com/css2?family=Figtree:wght@400;500;600;700&display=swap">
<style>
  :root {
    --backdrop: #dedede;
    --paper: #ffffff;
    --ink: #1e1e1e;
    --brand-dark: #3a3a3d;
    --brand-green: #5cba7c;
    --coral: #ef6a5e;
    --coral-shade: #db6056;
  }
  * { box-sizing: border-box; margin: 0; padding: 0; }
  html, body {
    width: 1200px;
    height: 800px;
    overflow: hidden;
    background: var(--backdrop);
    font-family: "Figtree", sans-serif;
  }
  .letterhead {
    position: absolute;
    left: 326px;
    top: 20px;
    width: 547px;
    height: 760px;
    background: var(--paper);
    overflow: hidden;
  }
  .brand {
    position: absolute;
    left: 16px;
    top: 22px;
    display: flex;
    align-items: center;
    gap: 12px;
  }
  .brand-dot {
    width: 40px;
    height: 40px;
    border-radius: 50%;
    background: var(--brand-green);
  }
  .brand-text { display: flex; flex-direction: column; }
  .brand-name {
    font-size: 28px;
    font-weight: 700;
    letter-spacing: 3px;
    color: var(--brand-dark);
    line-height: 1;
  }
  .brand-tagline {
    margin-top: 5px;
    font-size: 6.5px;
    font-weight: 600;
    letter-spacing: 1.3px;
    text-transform: uppercase;
    color: var(--brand-green);
  }
  .recipient {
    position: absolute;
    left: 28px;
    top: 204px;
    font-size: 17px;
    font-weight: 600;
    color: var(--brand-green);
  }
  .letter-body {
    position: absolute;
    left: 28px;
    top: 258px;
    width: 493px;
    font-size: 10.6px;
    line-height: 14.5px;
    color: var(--ink);
    text-align: justify;
  }
  .letter-body p.spaced { margin-bottom: 14.5px; }
  .closing {
    position: absolute;
    left: 28px;
    top: 538px;
    font-size: 10.6px;
    color: var(--ink);
  }
  .footer-band {
    position: absolute;
    left: 0;
    bottom: 0;
    width: 547px;
    height: 64px;
  }
</style>
</head>
<body>
  <main class="letterhead">
    <header class="brand">
      <span class="brand-dot"></span>
      <div class="brand-text">
        <span class="brand-name">NORDVALE</span>
        <span class="brand-tagline">Air Conditioning &amp; Refrigeration</span>
      </div>
    </header>

    <h1 class="recipient">Daniel Reyes</h1>

    <section class="letter-body">
      <p class="spaced">Lorem ipsum dolor sit amet, consectetur adipiscing sed do eiusmod tempor incididunt labore et dolore magna aliqua. Ut enim ad minim veniam, quis nostrud exercitation ullamco laboris nisi ut aliquip ex ea commodo consequat.</p>
      <p>Lorem ipsum dolor sit amet, consectetur adipiscing sed do eiusmod tempor incididunt labore et dolore magna aliqua. Ut enim ad minim veniam, quis nostrud exercitation ullamco laboris nisi ut aliquip ex ea commodo consequat. Duis aute irure dolor in reprehenderit in voluptate velit esse cillum</p>
      <p class="spaced">Lorem ipsum dolor sit amet, consectetur adipiscing sed do eiusmod tempor incididunt labore et dolore magna aliqua. consequat. Duis aute irure dolor in reprehenderit in voluptate velit esse cillum dolore eu fugiat nulla pariatur. Excepteur sint occaecat cupidatat non proident, sunt in culpa qui officia deserunt mollit,</p>
      <p>Lorem ipsum dolor sit amet, consectetur adipiscing sed do eiusmod tempor incididunt labore et dolore magna aliqua. Ut enim</p>
    </section>

    <p class="closing">Sincerely Yours</p>

    <svg class="footer-band" viewBox="0 0 547 64" aria-hidden="true">
      <polygon points="0,64 268,0 268,64" fill="var(--coral-shade)"/>
      <polygon points="268,0 547,64 268,64" fill="var(--coral)"/>
    </svg>
  </main>
</body>
</html>
```